Adwords Banner for unique handmade Jewelery

We need one Banner for our Jewelerys
in 4 sizes:
300x250px
336x280px
728x90px
160x600px

http://www.fenka-lauro.de/schmuck/2/

```html
<!DOCTYPE html>
<html lang="en">
<head>
<meta charset="utf-8">
<title>Fenka Lauro – Jewellery Banner Set</title>
<link rel="stylesheet" href="https://fonts.googleapis.com/css2?family=Crimson+Text:ital,wght@0,400;1,400&display=swap">
<style>
  :root {
    --board: #f1f1f1;
    --banner-top: #ffffff;
    --banner-bottom: #f5d3df;
    --rose: #c2508a;
    --rose-text: #c04a85;
    --logo-grey: #7a7478;
    --white: #ffffff;
    --shadow: rgba(0,0,0,0.18);
  }
  * { box-sizing: border-box; margin: 0; padding: 0; }
  html, body { width: 1200px; height: 1200px; overflow: hidden; }
  body { background: var(--board); font-family: "Crimson Text", Georgia, serif; position: relative; }

  .logo {
    position: absolute; display: flex; align-items: center; gap: 8px;
    color: var(--logo-grey); font-family: "Crimson Text", Georgia, serif;
    font-weight: 400; font-style: normal; white-space: nowrap; line-height: 1;
  }
  .logo__dot { border-radius: 50%; background: var(--rose); flex: none; }

  .hero-logo { left: 84px; top: 92px; font-size: 56px; }
  .hero-logo .logo__dot { width: 16px; height: 16px; }
  .hero-photo {
    position: absolute; left: 72px; top: 170px; width: 420px; height: 230px;
    background: radial-gradient(ellipse at 22% 62%, #7fd2d6 0 22%, transparent 38%),
                radial-gradient(ellipse at 64% 58%, #ea7fa6 0 18%, transparent 32%),
                linear-gradient(160deg, #f1f1f1 0%, #e3e6e8 100%);
  }

  .banner {
    position: absolute; overflow: hidden;
    background: linear-gradient(180deg, var(--banner-top) 0%, var(--banner-top) 30%, var(--banner-bottom) 100%);
    box-shadow: 0 1px 4px var(--shadow);
  }
  .banner .logo { font-size: 40px; }
  .banner .logo__dot { width: 12px; height: 12px; }
  .photo { position: absolute; }
  .band { position: absolute; left: 0; bottom: 0; width: 100%; }
  .band-text { position: absolute; color: var(--white); font-style: italic; line-height: 1.05; white-space: nowrap; }
  .headline { position: absolute; color: var(--rose-text); font-style: italic; line-height: 1; white-space: nowrap; }

  /* 336x280 */
  .banner--rectangle-large { left: 486px; top: 230px; width: 316px; height: 262px; }
  .banner--rectangle-large .logo { left: 24px; top: 18px; }
  .banner--rectangle-large .photo {
    left: 120px; top: 78px; width: 190px; height: 110px;
    background: radial-gradient(ellipse at 40% 65%, #6fcad0 0 20%, transparent 36%),
                radial-gradient(ellipse at 75% 70%, #e2769f 0 13%, transparent 26%);
  }
  .banner--rectangle-large .band-text { left: 14px; bottom: 8px; font-size: 22px; }

  /* 300x250 */
  .banner--rectangle { left: 448px; top: 568px; width: 354px; height: 296px; }
  .banner--rectangle .logo { left: 52px; top: 22px; }
  .banner--rectangle .photo {
    left: 112px; top: 78px; width: 210px; height: 150px;
    background: radial-gradient(ellipse at 38% 50%, #3fb3ba 0 26%, transparent 42%),
                radial-gradient(ellipse at 72% 52%, #d8dadc 0 24%, transparent 44%);
  }
  .banner--rectangle .band-text { left: 60px; bottom: 10px; text-align: right; }
  .banner--rectangle .band-text .small { font-size: 20px; }
  .banner--rectangle .band-text .big { font-size: 34px; }
  .banner--rectangle .band-text .sub { display: block; font-size: 17px; text-align: right; padding-right: 14px; }

  /* 160x600 */
  .banner--skyscraper { left: 816px; top: 230px; width: 170px; height: 634px; }
  .banner--skyscraper .headline { left: 10px; top: 12px; }
  .banner--skyscraper .headline .small { font-size: 20px; }
  .banner--skyscraper .headline .big { font-size: 32px; }
  .banner--skyscraper .headline .sub { display: block; font-size: 19px; padding-left: 48px; margin-top: 4px; }
  .banner--skyscraper .photo {
    left: 8px; top: 84px; width: 162px; height: 420px;
    background: radial-gradient(ellipse at 32% 20%, #e77aa2 0 14%, transparent 24%),
                radial-gradient(ellipse at 60% 45%, #66c6cc 0 12%, transparent 26%),
                radial-gradient(ellipse at 45% 80%, #3fb3ba 0 22%, transparent 36%),
                radial-gradient(ellipse at 85% 80%, #d4d6d8 0 16%, transparent 30%);
  }
  .banner--skyscraper .logo { left: 12px; bottom: 32px; font-size: 30px; }
  .banner--skyscraper .logo__dot { width: 10px; height: 10px; }

  /* 728x90 */
  .banner--leaderboard { left: 215px; top: 876px; width: 770px; height: 94px; }
  .banner--leaderboard .logo { left: 18px; top: 26px; }
  .banner--leaderboard .photo {
    left: 260px; top: 0; width: 360px; height: 94px;
    background: radial-gradient(ellipse at 28% 50%, #3fb3ba 0 18%, transparent 30%),
                radial-gradient(ellipse at 78% 50%, #3fb3ba 0 16%, transparent 28%),
                linear-gradient(90deg, transparent 0%, rgba(190,192,196,0.4) 50%, transparent 100%);
  }
  .banner--leaderboard .tag { position: absolute; right: 0; top: 0; width: 172px; height: 94px; }
  .banner--leaderboard .band-text { right: 14px; top: 16px; text-align: right; }
  .banner--leaderboard .band-text .small { font-size: 20px; }
  .banner--leaderboard .band-text .big { font-size: 32px; }
  .banner--leaderboard .band-text .sub { display: block; font-size: 19px; }
</style>
</head>
<body>

  <div class="logo hero-logo"><span class="logo__dot"></span>fenka lauro</div>
  <div class="hero-photo" role="img" aria-label="Close-up of a silver twisted chain with a turquoise and a pink glass heart bead"></div>

  <section class="banner banner--rectangle-large">
    <div class="logo"><span class="logo__dot"></span>fenka lauro</div>
    <div class="photo" role="img" aria-label="Silver chain with turquoise and pink glass heart beads"></div>
    <svg class="band" width="316" height="90" viewBox="0 0 316 90" aria-hidden="true">
      <path d="M0 0 C90 8 200 40 316 62 L316 90 L0 90 Z" fill="var(--rose)"/>
    </svg>
    <p class="band-text">The Heirloom<br>Glow Collection</p>
  </section>

  <section class="banner banner--rectangle">
    <div class="logo"><span class="logo__dot"></span>fenka lauro</div>
    <div class="photo" role="img" aria-label="Silver ring set with a turquoise glass stone"></div>
    <svg class="band" width="354" height="72" viewBox="0 0 354 72" aria-hidden="true">
      <path d="M0 22 C80 6 260 0 354 14 L354 72 L0 72 Z" fill="var(--rose)"/>
    </svg>
    <p class="band-text"><span class="small">The </span><span class="big">True Match</span><span class="sub">Collection</span></p>
  </section>

  <section class="banner banner--skyscraper">
    <p class="headline"><span class="small">The </span><span class="big">Radiant</span><span class="sub">Collection</span></p>
    <div class="photo" role="img" aria-label="Pink heart bead on chain, turquoise bead bracelet and turquoise glass ring"></div>
    <div class="logo"><span class="logo__dot"></span>fenka lauro</div>
  </section>

  <section class="banner banner--leaderboard">
    <div class="logo"><span class="logo__dot"></span>fenka lauro</div>
    <div class="photo" role="img" aria-label="Turquoise glass beads with silver spacers on a bracelet"></div>
    <svg class="tag" width="172" height="94" viewBox="0 0 172 94" aria-hidden="true">
      <path d="M28 0 L172 0 L172 94 L28 94 L0 47 Z" fill="var(--rose)"/>
    </svg>
    <p class="band-text"><span class="small">The </span><span class="big">Radiant</span><span class="sub">Collection</span></p>
  </section>

</body>
</html>
```